Letterhead and Envelope Design for Investment Company

We need a letterhead and envelope design.
We are a family owned investment company doing direct investments into other family owned businesses.
I have attached all our current marketing material including our logo for reference.

Our under construction website can be found here:
https://owen-darby-qk7m.sitebrella.example/
password: Marrowdale

Target Market(s)

Bankers, business owners, financial partners

Industry/Entity Type

Investment

Colors

Designer to choose colors to be used in the design.

Requirements
Must have
• Logo, and company information

```html
<!DOCTYPE html>
<html lang="en">
<head>
<meta charset="utf-8">
<title>Marrowdale Holdings Stationery</title>
<link href="https://fonts.googleapis.com/css2?family=Cinzel:wght@500&family=Questrial&display=swap" rel="stylesheet">
<style>
  :root {
    --backdrop: #b4b4b4;
    --paper: #f7f7f7;
    --ink: #151515;
    --ink-soft: #2a2a2a;
    --gold: #d9ad2c;
    --gold-light: #efcf62;
    --text: #555555;
    --cream: #eeeeee;
  }
  * { margin: 0; padding: 0; box-sizing: border-box; }
  html, body { width: 1200px; height: 1001px; overflow: hidden; }
  body {
    position: relative;
    background: radial-gradient(ellipse at 50% 30%, #c4c4c4 0%, var(--backdrop) 60%, #9e9e9e 100%);
    font-family: "Questrial", sans-serif;
  }
  .sheet { position: absolute; background: var(--paper); box-shadow: 0 2px 6px rgba(0,0,0,.25); }

  /* Letterhead */
  .letterhead { left: 82px; top: 187px; width: 503px; height: 710px; }
  .letterhead__header {
    position: absolute; left: 0; top: 0; width: 100%; height: 156px;
    background: radial-gradient(ellipse at 50% 40%, #2c2c2c 0%, var(--ink) 70%);
    border-bottom: 2px solid var(--gold);
  }
  .wordmark {
    font-family: "Cinzel", serif; font-weight: 500; color: var(--gold);
    text-align: center; letter-spacing: .02em; line-height: 1;
  }
  .letterhead__header .wordmark { position: absolute; left: 0; right: 0; top: 96px; font-size: 24px; }
  .wordmark small { display: block; font-size: .55em; margin-top: 4px; }
  .letterhead__body {
    position: absolute; left: 113px; top: 282px; width: 278px;
    font-size: 7.3px; line-height: 12.9px; color: var(--text); text-align: justify;
  }
  .letterhead__body p + p { margin-top: 13px; }
  .letterhead__footer {
    position: absolute; left: 0; bottom: 0; width: 100%; height: 68px;
    background: var(--ink); border-top: 2px solid var(--gold);
    font-family: "Cinzel", serif; font-size: 8.4px; line-height: 12px; color: var(--cream);
  }
  .footer__address { position: absolute; left: 41px; top: 14px; }
  .footer__contact { position: absolute; right: 29px; top: 14px; text-align: right; }
  .footer__divider { position: absolute; left: 249px; top: 8px; width: 1.5px; height: 46px; background: var(--gold); }

  /* Envelope front */
  .envelope-front { left: 626px; top: 192px; width: 499px; height: 248px; }
  .envelope-front .wordmark { position: absolute; left: 0; right: 0; top: 132px; font-size: 17px; }
  .envelope-front__url {
    position: absolute; left: 0; right: 0; top: 170px; text-align: center;
    font-family: "Cinzel", serif; font-size: 7px; color: var(--ink-soft);
  }

  /* Envelope back */
  .envelope-back { left: 624px; top: 475px; width: 499px; height: 250px; }
  .envelope-back__flap { position: absolute; left: 0; top: 0; }
  .envelope-back .wordmark { position: absolute; left: 0; right: 0; top: 47px; font-size: 13px; }
</style>
</head>
<body>

<section class="sheet letterhead">
  <header class="letterhead__header">
    <div class="wordmark">Marrowdale Holdings<small>Inc</small></div>
  </header>
  <div class="letterhead__body">
    <p>Lorem ipsum dolor sit amet, consectetuer adipiscing elit. Aenean commodo ligula eget dolor. Aenean massa. Cum sociis natoque penatibus et magnis dis parturient montes, nascetur ridiculus mus. Donec quam felis, ultricies nec, pellentesque eu, pretium quis, sem. Nulla consequat massa quis enim. Donec pede justo, fringilla vel, aliquet nec, vulputate eget, arcu. In enim justo, rhoncus ut, imperdiet a, venenatis vitae, justo. Nullam dictum felis eu pede mollis pretium. Integer tincidunt.</p>
    <p>Cras dapibus. Vivamus elementum semper nisi. Aenean vulputate eleifend tellus. Aenean leo ligula, porttitor eu, consequat vitae, eleifend ac, enim. Aliquam lorem ante, dapibus in, viverra quis, feugiat a, tellus. Phasellus viverra nulla ut metus varius laoreet. Quisque rutrum. Aenean imperdiet. Etiam ultricies nisi vel augue. Curabitur ullamcorper ultricies nisi. Nam eget dui. Etiam rhoncus. Maecenas tempus, tellus eget condimentum rhoncus, sem quam semper libero, sit amet adipiscing sem neque sed ipsum. Nam quam nunc, blandit vel, luctus</p>
  </div>
  <footer class="letterhead__footer">
    <div class="footer__address">Marrowdale Holdings, Inc.<br>48 Alder Row: Suite 210<br>Brookfield Falls, ST 00000</div>
    <div class="footer__divider"></div>
    <div class="footer__contact">P: 555-014-2290<br>www.marrowdaleholdings.example<br>inquiries@marrowdaleholdings.example</div>
  </footer>
</section>

<section class="sheet envelope-front">
  <div class="wordmark">Marrowdale Holdings<small>Inc</small></div>
  <div class="envelope-front__url">www.marrowdaleholdings.example</div>
</section>

<section class="sheet envelope-back">
  <svg class="envelope-back__flap" width="499" height="84" viewBox="0 0 499 84" aria-hidden="true">
    <defs>
      <radialGradient id="flapShade" cx="50%" cy="50%" r="60%">
        <stop offset="0" stop-color="#2e2e2e"/>
        <stop offset="1" stop-color="#141414"/>
      </radialGradient>
    </defs>
    <path d="M0 0 H499 L490 72 Q489 79 482 79 H17 Q10 79 9 72 Z" fill="url(#flapShade)"/>
    <path d="M9 72 Q10 79 17 79 H482 Q489 79 490 72" fill="none" stroke="#d9ad2c" stroke-width="2"/>
  </svg>
  <div class="wordmark">Marrowdale Holdings<small>Inc</small></div>
</section>

</body>
</html>
```